Business Card Design Project

Looking for a business card that our customers will remember. We are a high end Travel Agency.
Need a re-memorable classy business card.
Both sides full color.
Must have the following details.
Voyage Harbor Logo (see attached)
4B Wattle Lane
Penhurst Sydney NSW 2241
Phone: 02 9471 3652
Fax: 02 9563 4417
sales@voyageharbor-example.com.au
Consultant Name
Anything else you think we need

```html
<!DOCTYPE html>
<html lang="en">
<head>
<meta charset="utf-8">
<title>Voyage Harbor – Business Card</title>
<link rel="stylesheet" href="https://fonts.googleapis.com/css2?family=Noto+Sans:wght@400;700&family=Arimo&display=swap">
<style>
  :root {
    --page: #ffffff;
    --card-edge: #222222;
    --ink: #111111;
    --brand: #1f5078;
    --accent-yellow: #f2c21b;
    --map-lilac: #dcdff0;
    --tile-pink: #d9479a;
    --tile-green: #8cc63f;
    --tile-lime: #cddc39;
    --tile-cyan: #3bb8cc;
    --tile-blue: #1f63a8;
    --tile-yellow: #f4c520;
  }
  * { box-sizing: border-box; margin: 0; padding: 0; }
  html, body {
    width: 866px; height: 1200px; overflow: hidden;
    background: var(--page);
  }
  body { position: relative; font-family: "Noto Sans", sans-serif; color: var(--ink); }

  .card {
    position: absolute; left: 64px; width: 754px; height: 452px;
    border: 1.5px solid var(--card-edge); background: var(--page); overflow: hidden;
  }
  .card--front { top: 55px; }
  .card--back  { top: 694px; left: 67px; height: 453px; }

  .world-map {
    position: absolute;
    background: radial-gradient(ellipse at 50% 55%, var(--map-lilac) 0%, rgba(220,223,240,0.7) 55%, rgba(220,223,240,0) 80%);
  }
  .card--front .world-map { left: 92px; top: 74px; width: 662px; height: 378px; }
  .card--back  .world-map { left: 0; top: 120px; width: 754px; height: 333px; }

  .tile-field { position: absolute; }
  .tile-field--top-left {
    left: 0; top: 0; width: 222px; height: 204px;
    background:
      linear-gradient(135deg, rgba(217,71,154,0.35), rgba(205,220,57,0.3) 45%, rgba(59,184,204,0.25) 75%, rgba(255,255,255,0) 100%);
  }
  .tile-field--bottom-right {
    right: 0; bottom: 0; width: 300px; height: 360px;
    background:
      linear-gradient(315deg, var(--tile-pink) 0%, var(--tile-green) 25%, var(--tile-lime) 45%, rgba(59,184,204,0.6) 65%, rgba(255,255,255,0) 90%);
  }
  .card--back .tile-field--top-left {
    width: 315px; height: 300px; opacity: 0.7;
  }
  .card--back .tile-field--bottom-right {
    width: 194px; height: 243px; opacity: 0.45;
  }

  .brand-name {
    position: absolute; display: flex; align-items: center; gap: 12px;
    font-weight: 400; color: var(--brand); white-space: nowrap;
  }
  .brand-name__dot {
    width: 16px; height: 16px; border-radius: 50%; background: var(--accent-yellow);
  }
  .card--front .brand-name { left: 220px; top: 26px; font-size: 42px; }
  .card--back  .brand-name { left: 46px; top: 180px; font-size: 56px; }

  .consultant-name {
    position: absolute; left: 0; width: 754px; top: 203px;
    text-align: center; font-weight: 700; font-size: 40px; letter-spacing: 0.3px;
  }

  .contact {
    position: absolute; left: 15px; top: 350px;
    font-size: 19px; line-height: 22px;
  }
  .contact__address { margin-top: 4px; }

  .company-note {
    position: absolute; left: 180px; top: 296px;
    font-family: "Arimo", sans-serif; font-size: 22px; letter-spacing: 0.2px;
  }
</style>
</head>
<body>

  <section class="card card--front">
    <div class="world-map" role="img" aria-label="Faint world map in soft lilac"></div>
    <div class="tile-field tile-field--top-left" role="img" aria-label="Scattered pastel mosaic squares"></div>
    <div class="tile-field tile-field--bottom-right" role="img" aria-label="Bright mosaic of coloured squares"></div>

    <div class="brand-name"><span>Voyage Harbor</span><span class="brand-name__dot"></span></div>

    <h1 class="consultant-name">Consultant Name</h1>

    <address class="contact" style="font-style:normal">
      <div class="contact__phone">Phone: 02 9471 3652</div>
      <div class="contact__fax">Fax: 02 9563 4417</div>
      <div class="contact__email">sales@voyageharbor-example.com.au</div>
      <div class="contact__address">4B Wattle Lane&nbsp; Penhurst Sydney NSW 2241</div>
    </address>
  </section>

  <section class="card card--back">
    <div class="world-map" role="img" aria-label="Faint world map in soft lilac"></div>
    <div class="tile-field tile-field--top-left" role="img" aria-label="Scattered pastel mosaic squares"></div>
    <div class="tile-field tile-field--bottom-right" role="img" aria-label="Pale mosaic of coloured squares"></div>

    <div class="brand-name"><span>Voyage Harbor</span><span class="brand-name__dot"></span></div>

    <p class="company-note">INSTRUCTION FOR THE COMPANY</p>
  </section>

</body>
</html>
```